Seven Quiet Steps to Lift the Final Offer on YOUR House - MERVA Real Estate

I have written an E-Book that is called "Seven Quiet Steps to Lift the Final Offer on Your House." The E-Book will be available as a FREE download from my MERVA Real Estate landing page, and also from a Facebook campaign that will be commencing in early September.

The E-Book content is in the WORD document below - I now need for it to be made to look more professional and suitable for publishing and placed on my landing page for download. Please review and send me some proposals for this e-book to be a bit more eye catching and appealing than just a WORD doc.

My MERVA Real Estate landing page is still under development and you can see the what is close to the final proposal here:

http://www.brell-tovan.com.au/merva/

The cover of the E-Book is at the bottom of the page. Please review and give the internals the sale look and feel.

Target Market(s)

Home and Property Owners in the middle ring Eastern Suburbs of Melbourne - approximately 15 - 30 km's from the central business district. The area is a very family oriented area and features mostly houses that are 3 or 4 bedroom - with some larger properties that are five or more bedrooms. The area is quite an expensive suburban community and house prices range between the low of $1,000,000 to a high of more than $2,500,000. The predominant cultural group that buys in this area are Chinese and Chinese Australian buyers. The predominant group who are selling are usually Australians of a white anglo-saxon background. Other groups are of Asian sub continent background (Indian / Sri Lankan/ Pakistan). All are families that are attracted to the area because of the great schools, good shopping, leisure facilities (parks, pools, courts etc), and excellent public and road transport infrastructure. Read the content of my e-book - it tells you every thing you need to know :)

Industry/Entity Type

Real Estate

Colors

Designer to choose colors to be used in the design.

Requirements
Must have
• Once completed the layout should not be too busy - it should be easy to read. I guess then the statement "less is more" is applicable.
• I will probably print a number of copies of this book for distribution as well - so please consider print attributes in the design.
• IMPORTANT: as for any e-book offering specialist advice, the MAIN reason for the book is for the generation of sales leads and to establish the author as a subject matter expert on the topic. Please consider this in your design elements. BUT - the book should also not come across as 1 big advertisement either. Subtle but impactful are well chosen words to describe how it should present.
Nice to have
• MERVA Real Estate branding on every page - to re-inforce the message.
Should not have
• No need for animations or illustrations/

```html
<!DOCTYPE html>
<html lang="en">
<head>
<meta charset="utf-8">
<title>Seven Quiet Steps to Lift the Final Offer on YOUR House - MERVA Real Estate</title>
<link rel="stylesheet" href="https://fonts.googleapis.com/css2?family=Lato:ital,wght@0,400;0,700;0,900;1,400&family=Roboto+Condensed:wght@300;400;700&display=swap">
<style>
:root{
  --teal:#3dbd8f;
  --ink:#1e1e1e;
  --text:#2b2b2b;
  --paper:#ffffff;
  --bg:#ffffff;
  --band:#2a2a2a;
  --sky-top:#2f6cc0;
  --sky-low:#8fb2dc;
}
*{margin:0;padding:0;box-sizing:border-box}
html,body{width:1200px;height:1200px;overflow:hidden;background:var(--bg)}
body{position:relative;font-family:"Lato",sans-serif;color:var(--text)}
.page{position:absolute;top:216px;width:542px;height:766px;background:var(--paper);box-shadow:0 0 6px rgba(0,0,0,.22);overflow:hidden}
.page--one{left:42px}
.page--two{left:616px}
.abs{position:absolute}
.brand{position:absolute;left:330px;top:26px;width:182px;text-align:right}
.brand__name{font-family:"Lato",sans-serif;font-weight:900;font-size:60px;line-height:60px;color:var(--ink);letter-spacing:1px}
.brand__tag{font-family:"Lato",sans-serif;font-size:9px;letter-spacing:10.4px;color:var(--ink);margin-top:2px;margin-right:-10px}
.hero{position:absolute;left:0;top:0}
.hero__title{position:absolute;left:60px;top:92px;color:#fff;font-family:"Lato",sans-serif;font-weight:700;font-size:21px;line-height:26px;text-align:center;text-shadow:0 1px 2px rgba(0,0,0,.35)}
.heading{position:absolute;left:32px;font-family:"Roboto Condensed",sans-serif;font-weight:700;color:var(--teal);font-size:17px;letter-spacing:.2px}
.body{font-size:7.6px;line-height:9.8px;text-align:justify}
.body p+p{margin-top:8px}
.lead{position:absolute;left:33px;top:345px;width:477px}
.dark{position:absolute;left:0;top:436px;width:542px;height:228px;background:#0f0f0f;color:#eee}
.dark__title{position:absolute;left:32px;top:12px;color:var(--teal);font-size:12px}
.dark__intro{position:absolute;left:33px;top:34px;width:477px}
.col{position:absolute;top:69px;width:230px}
.col--a{left:33px}
.col--b{left:279px}
.feat{position:relative;padding-left:15px;margin-bottom:9px}
.feat svg{position:absolute;left:0;top:0}
.hl{color:var(--teal)}
.closing{position:absolute;left:33px;top:683px;width:477px}
.footer{position:absolute;left:0;top:0}
.footer__url{position:absolute;left:190px;top:729px;font-size:8px;letter-spacing:3px;color:#fff}
.footer__num{position:absolute;left:490px;top:721px;font-family:"Roboto Condensed",sans-serif;font-weight:300;font-size:21px;color:var(--teal)}
.cols2{position:absolute;top:347px;width:229px}
.cols2--a{left:33px}
.cols2--b{left:280px}
.quote{position:absolute;left:33px;top:462px;width:476px;font-style:italic;font-size:7.4px;line-height:9.6px}
.text-block{position:absolute;left:33px;top:516px;width:477px}
.sub{position:absolute;left:32px;top:607px;font-family:"Roboto Condensed",sans-serif;font-weight:400;font-size:13.5px;color:var(--ink)}
.pill{position:absolute;left:0;top:631px;width:114px;height:13px;background:var(--teal);border-radius:0 7px 7px 0;color:#fff;font-size:9px;line-height:13px;padding-left:32px}
.basics-a{position:absolute;left:33px;top:654px;width:229px}
.basics-b{position:absolute;left:280px;top:611px;width:229px}
</style>
</head>
<body>

<section class="page page--one">
  <svg class="hero" width="542" height="310" viewBox="0 0 542 310">
    <defs>
      <linearGradient id="photoA" x1="0" y1="0" x2="0" y2="1">
        <stop offset="0" stop-color="#2c66bd"/>
        <stop offset=".38" stop-color="#8aaedb"/>
        <stop offset=".55" stop-color="#8d5a44"/>
        <stop offset=".78" stop-color="#4b7a36"/>
        <stop offset="1" stop-color="#6b9f3e"/>
      </linearGradient>
    </defs>
    <polygon role="img" aria-label="Photo of a single storey brick family home with a garden" points="0,108 164,40 286,108 542,108 542,296 0,296" fill="url(#photoA)"/>
    <polyline points="0,106 164,37 287,106 542,106" fill="none" stroke="var(--ink)" stroke-width="4"/>
    <rect x="0" y="296" width="542" height="5" fill="var(--ink)"/>
  </svg>
  <div class="hero__title">City of Monash<br>&amp; City of Whitehorse</div>

  <div class="brand"><div class="brand__name">MERVA</div><div class="brand__tag">REAL ESTATE</div></div>

  <h1 class="heading" style="top:324px">SEVEN QUIET STEPS TO LIFT THE FINAL OFFER ON YOUR HOUSE</h1>

  <div class="lead body">
    <p>So after much consideration you have made the decision to sell your property. For some of you the home may have held many long and happy memories. For others it may have been a property used purely as an investment vehicle to greater wealth. Unfortunately for some others it may be necessary to sell due to life challenges – these may be financial issues, a marriage breakdown or even the passing away of a relative. Whatever the reason and your motivation for selling – once the decision to sell is made, the most important end result is to get for your property the best possible price available in the market place.</p>
    <p>In my free e-book – you will find Seven Quiet Steps to Lift the Final Offer on Your House. It includes some useful tips to help you prepare your property to be put on the market for sale. Then once it is ready – what to do to extract top dollar for the sale of your home.</p>
  </div>

  <div class="dark">
    <div class="dark__title">By the way….CONGRATULATIONS on your choice of location:</div>
    <p class="dark__intro body">The desirable and leafy City of Monash and City of Whitehorse are exceptionally popular residential localities – and it is little wonder when you consider all that they offer to the modern family. The standout features of these two great municipalities include:</p>
    <div class="col col--a body">
      <div class="feat"><svg width="10" height="10" viewBox="0 0 10 10"><circle cx="5" cy="5" r="4.3" fill="none" stroke="var(--teal)"/><path d="M2.8 5.1l1.5 1.5 3-3" fill="none" stroke="var(--teal)"/></svg><span class="hl">Superb education options</span> - some of Melbourne's leading government and private primary and secondary schools are located within the boundaries of the City of Monash and the City of Whitehorse. There are also excellent tertiary education choices present with Ashcombe University (Burwood campus), Southvale University (Clayton campus), Kelverton Institute, and the Eastern Services Academy, amongst others handily located in the region. And the range of great childcare and Kindergarten options round out an amazing list of K-12 education options and beyond for local residents.</div>
      <div class="feat"><svg width="10" height="10" viewBox="0 0 10 10"><circle cx="5" cy="5" r="4.3" fill="none" stroke="var(--teal)"/><path d="M2.8 5.1l1.5 1.5 3-3" fill="none" stroke="var(--teal)"/></svg><span class="hl">Outstanding shopping</span> exists and includes shopping centres like The Orchard, Hillcrest Village, Cedarwood Village, Brandle Park Plaza, Fernhill Chase, Boxley Central as well as a number of smaller strip shopping and local centres.</div>
    </div>
    <div class="col col--b body">
      <div class="feat"><svg width="10" height="10" viewBox="0 0 10 10"><circle cx="5" cy="5" r="4.3" fill="none" stroke="var(--teal)"/><path d="M2.8 5.1l1.5 1.5 3-3" fill="none" stroke="var(--teal)"/></svg><span class="hl">Beautiful parks, gardens, trails and outdoor leisure facilities</span> including Jells Park, Valley Reserve, Blackburn Lake Sanctuary, Scotchman's Creek Linear Trail, Hartdale Golf Club, Rivermead Golf Course, Glenmere Public Golf Course and many other sporting facilities and grounds.</div>
      <div class="feat"><svg width="10" height="10" viewBox="0 0 10 10"><circle cx="5" cy="5" r="4.3" fill="none" stroke="var(--teal)"/><path d="M2.8 5.1l1.5 1.5 3-3" fill="none" stroke="var(--teal)"/></svg>A large number of <span class="hl">public transport choices</span> for commuters and students spread right across the region including trains, trams and buses depending on your location.</div>
      <div class="feat"><svg width="10" height="10" viewBox="0 0 10 10"><circle cx="5" cy="5" r="4.3" fill="none" stroke="var(--teal)"/><path d="M2.8 5.1l1.5 1.5 3-3" fill="none" stroke="var(--teal)"/></svg><span class="hl">Excellent freeway and road infrastructure</span> that is continuously evolving and includes the Monash Freeway, Eastway, and the Eastern Freeway. All parts of Melbourne are easily accessible from the City of Monash and the City of Whitehorse.</div>
    </div>
  </div>

  <p class="closing body">Education, shopping convenience, leisure facilities and transport infrastructure form the back bone of any desirable community – and the attraction of families, investors and developers to these popular and well established residential areas ensure that the foundation for interest in your property is already in place. So in order for your home to sell well and achieve the best possible price, here are the Seven Quiet Steps to Lift the Final Offer on Your House to help you on your journey.</p>

  <svg class="footer" width="542" height="766" viewBox="0 0 542 766">
    <rect x="0" y="728" width="542" height="14" fill="var(--teal)"/>
    <rect x="0" y="742" width="542" height="10" fill="var(--band)"/>
    <polygon points="462,752 478,718 542,718 542,752" fill="var(--band)"/>
  </svg>
  <div class="footer__url">www.mervarealestate.com.au</div>
  <div class="footer__num">01</div>
</section>

<section class="page page--two">
  <svg class="hero" width="542" height="310" viewBox="0 0 542 310">
    <defs>
      <linearGradient id="photoB" x1="0" y1="0" x2="0" y2="1">
        <stop offset="0" stop-color="#2a5fb5"/>
        <stop offset=".35" stop-color="#9ab6da"/>
        <stop offset=".5" stop-color="#8c8780"/>
        <stop offset=".82" stop-color="#7c756c"/>
        <stop offset="1" stop-color="#9a8f82"/>
      </linearGradient>
    </defs>
    <polygon role="img" aria-label="Photo of a modern two storey rendered family home" points="0,108 164,40 286,108 542,108 542,296 0,296" fill="url(#photoB)"/>
    <polyline points="0,106 164,37 287,106 542,106" fill="none" stroke="var(--ink)" stroke-width="4"/>
    <rect x="0" y="296" width="542" height="5" fill="var(--ink)"/>
  </svg>

  <div class="brand"><div class="brand__name">MERVA</div><div class="brand__tag">REAL ESTATE</div></div>

  <h2 class="heading" style="top:322px">1. PROPERTY PRESENTATION:</h2>

  <div class="cols2 cols2--a body">
    <b>Like any product</b> – the newer, the cleaner, the shinier, and the better presented a property is for sale...then the more interest it will attract from prospective Buyers.<br>
    The more Buyer interest that a property attracts...the more competition around the purchase price that will be created.<br>
    And Buyer competition is fantastic if you know how to harness it to achieve the best possible sale price. But where is it that you should begin and how?
  </div>
  <div class="cols2 cols2--b body">
    <b>So let's start at the very beginning</b> – property preparation and presentation for sale.<br>
    It is important to state that very few people actually live in the manner that a house is presented for sale. In most instances what you see at homes that are open for Buyer inspection is the end result of a lot of hard work on behalf of the Vendor and others.<br>
    So don't be concerned – how ever and whatever your home looks like now...it can be transformed to maximize its appeal to Buyers.
  </div>

  <svg class="abs" style="left:0;top:0" width="542" height="510" viewBox="0 0 542 510">
    <circle cx="42" cy="446" r="9" fill="none" stroke="var(--teal)" stroke-width="1.4"/>
    <text x="42" y="452" text-anchor="middle" font-family="Lato,sans-serif" font-weight="900" font-size="13" fill="var(--teal)">“</text>
    <line x1="54" y1="448" x2="509" y2="448" stroke="#777" stroke-width=".6"/>
    <line x1="33" y1="488" x2="486" y2="488" stroke="#777" stroke-width=".6"/>
    <circle cx="498" cy="487" r="9" fill="none" stroke="var(--teal)" stroke-width="1.4"/>
    <text x="498" y="493" text-anchor="middle" font-family="Lato,sans-serif" font-weight="900" font-size="13" fill="var(--teal)">”</text>
  </svg>
  <p class="quote">Vendor's will always see all of the great and wonderful aspects of their property in an effort to create value and push up the price; a Buyer will always tell you everything that is wrong in an effort to drive down the price."</p>

  <div class="text-block body">
    <p>The whole process of buying and selling property is very psychological and highly emotional for most people, so it is very important for Vendors to place themselves in the shoes of a Buyer when running a critical eye across the presentation preparations.</p>
    <p>Your property should be polished, displayed and presented to the highest possible standard. That standard will be different for everyone – factoring in age, ability, financial capacity, the size of family, number of pets and so on.</p>
    <p>In addition - every property is different, and every property has it's own features and personality – what's important is to amplify the positives and minimize the impact of the negatives throughout the home.</p>
  </div>

  <h3 class="sub">Let's look at some of the basics:</h3>
  <div class="pill">Curbside appeal</div>

  <div class="basics-a body">
    <p>First impressions count - stand outside at the front of your house on the street and look at your house with a critical eye. Does your home stand out as a welcoming and "happy" place to arrive at?</p>
    <p style="margin-top:12px">Tidy the gardens, mow the lawns, repair the gutters, paint under the eaves of the roof, clean the windows, repair the cracks in the</p>
  </div>
  <div class="basics-b body">
    <p>cement driveways and do some basic landscaping such as adding mulch to garden beds (my personal preference for mulch is black tan bark – but other varieties are just as effective). You will find all these tasks make a huge difference to the exterior look and feel of your property.</p>
    <p style="margin-top:10px">If your property has a fence, then clean it and paint it. Cut back any overgrown trees and bushes, trim and shape the edges of pathways, and clear and remove all rubbish (including rubbish bins) from the front of the house.</p>
  </div>

  <svg class="footer" width="542" height="766" viewBox="0 0 542 766">
    <rect x="0" y="728" width="542" height="14" fill="var(--teal)"/>
    <rect x="0" y="742" width="542" height="10" fill="var(--band)"/>
    <polygon points="462,752 478,718 542,718 542,752" fill="var(--band)"/>
  </svg>
  <div class="footer__url">www.mervarealestate.com.au</div>
  <div class="footer__num">02</div>
</section>

</body>
</html>
```